hi all

Im after a new age looking business card with my company logo on it

must include these details, I would like the PH and Email to be symbols

If the colours used for card could be kept within the colours used in logo that I have supplied that would be great, if another colour is to be used dark grey would be ok. no light bulbs etc thanks

Details below to be incorporated on card

Damian Holloway

Lic E871302

PH 0219647381

E info@brightvaleelectrical.example.nz

Domestic Commercial Industrial Electricians

```html
<!DOCTYPE html>
<html lang="en">
<head>
<meta charset="utf-8">
<title>Brightvale Electrical – Business Card</title>
<link href="https://fonts.googleapis.com/css2?family=Orbitron:wght@700&family=Raleway:wght@400;500&display=swap" rel="stylesheet">
<style>
  :root {
    --stage: #2a2a2a;
    --card-black: #050505;
    --card-white: #ffffff;
    --brand-blue: #0a74c2;
    --text-white: #ffffff;
  }
  * { margin: 0; padding: 0; box-sizing: border-box; }
  html, body {
    width: 1200px; height: 900px; overflow: hidden;
    background: var(--stage);
  }
  .canvas {
    position: relative; width: 1200px; height: 900px;
    display: flex; flex-direction: column; align-items: center; justify-content: center; gap: 40px;
  }
  .card {
    position: relative; width: 620px; height: 354px; overflow: hidden;
    box-shadow: 0 12px 30px rgba(0,0,0,.45);
  }
  .card--front { background: var(--card-black); }
  .card--back { background: var(--card-white); }

  .brand { display: flex; align-items: center; gap: 16px; }
  .brand__dot {
    flex: none; border-radius: 50%; border: 4px solid var(--brand-blue);
  }
  .brand__name {
    font-family: "Orbitron", sans-serif; font-weight: 700; color: var(--brand-blue);
    line-height: 1; text-transform: uppercase;
  }
  .brand__name span { display: block; }

  .card--front .brand { position: absolute; left: 150px; top: 108px; }
  .card--front .brand__dot { width: 56px; height: 56px; }
  .card--front .brand__line1 { font-size: 42px; letter-spacing: 1px; }
  .card--front .brand__line2 { font-size: 18px; letter-spacing: 9px; margin-top: 8px; text-align: right; }

  .tagline {
    position: absolute; left: 0; right: 0; top: 268px; text-align: center;
    font-family: "Raleway", sans-serif; font-weight: 500; font-size: 15px;
    letter-spacing: 1px; color: var(--text-white); text-transform: uppercase;
  }

  .card--back .brand { position: absolute; left: 32px; top: 34px; gap: 10px; }
  .card--back .brand__dot { width: 34px; height: 34px; border-width: 3px; }
  .card--back .brand__line1 { font-size: 28px; }
  .card--back .brand__line2 { font-size: 12px; letter-spacing: 6px; margin-top: 6px; text-align: right; }

  .wave { position: absolute; inset: 0; width: 100%; height: 100%; }

  .contact {
    position: absolute; right: 32px; top: 230px; text-align: right;
    font-family: "Raleway", sans-serif; color: var(--text-white);
  }
  .contact__name {
    font-family: "Orbitron", sans-serif; font-weight: 700; font-size: 19px;
    letter-spacing: 2px; color: var(--brand-blue); text-transform: uppercase; margin-bottom: 12px;
    line-height: 24px;
  }
  .contact__row {
    display: flex; justify-content: flex-end; align-items: center; gap: 10px;
    font-size: 15px; line-height: 22px;
  }
  .contact__icon { width: 16px; height: 16px; flex: none; }
  .contact__licence { margin-top: 10px; font-size: 17px; line-height: 22px; margin-right: 26px; }
  .contact__licence-label { color: var(--brand-blue); margin-right: 4px; }
</style>
</head>
<body>
<main class="canvas">

  <section class="card card--front" aria-label="Card front">
    <div class="brand">
      <div class="brand__dot"></div>
      <div class="brand__name"><span class="brand__line1">Brightvale</span><span class="brand__line2">Electrical</span></div>
    </div>
    <p class="tagline">Domestic Commercial Industrial Electricians</p>
  </section>

  <section class="card card--back" aria-label="Card back">
    <svg class="wave" viewBox="0 0 620 354" preserveAspectRatio="none" aria-hidden="true">
      <path d="M0,262 C110,250 200,228 285,196 L285,202 C200,236 110,262 0,276 Z" fill="var(--brand-blue)"/>
      <path d="M0,312 C170,296 320,180 470,152 C540,140 590,160 620,176 L620,354 L0,354 Z" fill="var(--brand-blue)"/>
      <path d="M0,326 C180,312 330,200 475,178 C545,168 592,184 620,204 L620,354 L0,354 Z" fill="var(--card-black)"/>
    </svg>
    <div class="brand">
      <div class="brand__dot"></div>
      <div class="brand__name"><span class="brand__line1">Brightvale</span><span class="brand__line2">Electrical</span></div>
    </div>
    <div class="contact">
      <p class="contact__name">Damian Holloway</p>
      <p class="contact__row">021 964 7381
        <svg class="contact__icon" viewBox="0 0 16 16" aria-label="Phone"><circle cx="8" cy="8" r="7" fill="none" stroke="var(--brand-blue)" stroke-width="1.2"/><path d="M5.3,4.5 L6.6,4.3 L7.2,6.2 L6.4,6.9 C6.9,8 7.8,8.9 8.9,9.4 L9.6,8.6 L11.5,9.2 L11.3,10.5 C8,10.7 5.1,7.8 5.3,4.5 Z" fill="var(--brand-blue)"/></svg>
      </p>
      <p class="contact__row">info@brightvaleelectrical.example.nz
        <svg class="contact__icon" viewBox="0 0 16 16" aria-label="Email"><rect x="1.5" y="3.5" width="13" height="9" fill="none" stroke="var(--brand-blue)" stroke-width="1.2"/><path d="M1.5,3.5 L8,9 L14.5,3.5" fill="none" stroke="var(--brand-blue)" stroke-width="1.2"/></svg>
      </p>
      <p class="contact__licence"><span class="contact__licence-label">LIC</span> E871302</p>
    </div>
  </section>

</main>
</body>
</html>
```